Nimbo58.com.au Website and company image design

We are looking for an exceptional website designer / company to work with our new Australian Hosting Company

Nimbo58 is a new Cloud Hosting company launching in Australia that provides Scalable, On Demand computing resources to the Australian Market Place. Scalable, On Demand ocmputing is a nice way of saying fully scalable / redundant Virtual Private Server.

We require a full company image to be developed along with a Logo and Website. There is scope for ongoing development (preferred) for the successful candidate.

Website developement will require extensive jQuery ability (sliders for ordering etc (see: http://www.hostrix-example.com.au/virtual-dedicated-servers/253/zar_vps.html).

Please communicate directly with me to establish full website scope and request further documentation / content.

Target Market(s)

Website Designers, programmers, technicians and large companies

Industry/Entity Type

It Company

Requirements
Must have
• Slider ordering system such as http://www.hostrix-example.com.au/virtual-dedicated-servers/253/zar_vps.html

Nice to have
• CMS backend system
Should not have
• Should NOT be a monster template copy!!!

```html
<!DOCTYPE html>
<html lang="en">
<head>
<meta charset="utf-8">
<title>Nimbo58 – Cloud Hosting</title>
<link rel="stylesheet" href="https://fonts.googleapis.com/css2?family=Source+Sans+3:ital,wght@0,300;0,400;0,600;1,400&display=swap">
<style>
:root{
  --brand:#8b1a46;
  --topbar:#2c2f36;
  --ink:#3a3e47;
  --text:#4a4a4a;
  --muted:#a9a9a9;
  --rule:#dcdcdc;
  --panel:#efefef;
  --band:#f4f4f4;
  --footer:#e8e8e8;
  --base:#d9d9d9;
}
*{margin:0;padding:0;box-sizing:border-box}
html,body{width:939px;height:1200px;overflow:hidden}
body{position:relative;background:#fff;font-family:"Source Sans 3",sans-serif;color:var(--text)}
.abs{position:absolute}

.topbar{left:0;top:0;width:939px;height:35px;background:var(--topbar)}
.topbar-link{top:0;height:35px;display:flex;align-items:center;gap:6px;color:#e8e8e8;font-size:10.5px}
.topbar-link svg{width:12px;height:12px;fill:#d8d8d8}

.brand{left:84px;top:52px;display:flex;align-items:center;gap:8px;font-size:34px;font-weight:600;color:var(--brand)}
.brand-dot{width:22px;height:22px;border-radius:50%;background:var(--brand)}

.nav-rule{left:276px;top:90px;width:576px;height:2px;background:var(--brand)}
.nav-item{top:70px}
.nav-item .label{font-size:12px;color:var(--brand);letter-spacing:.2px}
.nav-item .sub{margin-top:10px;font-size:9.5px;color:#333}
.nav-sep{top:70px;width:1px;height:16px;background:var(--brand)}
.header-rule{left:88px;top:135px;width:765px;height:1px;background:#ececec}

.hero{left:0;top:140px;width:939px;height:248px;background:linear-gradient(180deg,#fff 0%,#f1f1f1 80%,#fff 100%)}
.hero-art{left:132px;top:156px;width:200px;height:200px;background:linear-gradient(90deg,#2a2d33,#5a5f68 45%,#23262b);border-radius:3px}
.hero-title{left:346px;top:172px;font-size:40px;font-weight:300;color:var(--ink);letter-spacing:-.3px}
.hero-rule{left:346px;top:230px;width:324px;height:1px;background:#bdbdbd}
.hero-tags{left:350px;top:238px;font-size:10.5px;color:#555;word-spacing:1px}
.hero-tags span{margin:0 10px;color:#777}
.hero-btn{left:690px;top:234px;width:146px;height:22px;background:#c8c8c8;color:#fff;font-size:10px;display:flex;align-items:center;justify-content:center}
.slide-dot{top:309px;width:16px;height:16px;border-radius:50%;border:1px solid #cfcfcf;background:#fff;font-size:7.5px;color:#555;display:flex;align-items:center;justify-content:center}
.slide-dot.active{color:var(--brand)}

.h1{left:88px;top:400px;font-size:16px;color:#2f2f2f}
.h1 small{font-size:15px;color:var(--muted);margin-left:10px;font-weight:300}
.h1-rule{left:88px;top:432px;width:505px;height:1px;background:var(--rule)}
.h2{left:88px;top:444px;font-size:11.5px;color:var(--brand)}
.h2 strong{font-size:15px;font-weight:400;margin-left:6px}
.h2 small{font-size:11.5px;color:var(--muted);margin-left:6px}
.intro{left:88px;top:471px;width:505px;font-size:9.3px;line-height:15.6px;text-align:justify}
.offer{left:608px;top:404px;width:244px;height:114px;background:linear-gradient(120deg,#f3f3f3 0%,#8e9196 45%,#2b2d31 100%);border:1px solid #d0d0d0}
.offer-tab{left:734px;top:482px;width:118px;height:22px;background:rgba(245,245,245,.92);border-radius:11px 0 0 11px;font-size:11.5px;color:#222;display:flex;align-items:center;justify-content:center}
.body-copy{left:88px;top:539px;width:765px;font-size:9.3px;line-height:15.7px;text-align:justify}

.rule{left:88px;width:765px;height:1px;background:var(--rule)}
.sample-h1{left:88px;top:733px;font-size:14.5px;color:#2f2f2f}
.sample-h2{left:88px;top:758px;font-size:10.5px;color:var(--brand)}
.sample-p{left:88px;top:782px;font-size:9px;color:#333}

.avatar{left:94px;top:826px;width:65px;height:70px;border:1px solid #ccc;background:linear-gradient(180deg,#e8e4df,#c9b9a8 60%,#33404f);}
.avatar-name{left:94px;top:903px;width:65px;text-align:center;font-size:10px;color:var(--brand)}
.testimonial{left:178px;top:826px;width:669px;height:90px;background:var(--panel);border-radius:4px}
.testimonial-arrow{left:170px;top:838px;width:0;height:0;border-top:8px solid transparent;border-bottom:8px solid transparent;border-right:8px solid var(--panel)}
.testimonial-title{left:194px;top:834px;font-size:14.5px;color:#2f2f2f}
.testimonial-rule{left:194px;top:862px;width:638px;height:1px;background:#d8d8d8}
.testimonial-quote{left:198px;top:872px;width:640px;font-size:9.3px;line-height:16px;font-style:italic;color:#555}
.testimonial-quote b{font-size:13px;color:#888;font-style:normal;margin:0 4px}

.feeds{left:0;top:940px;width:939px;height:66px;background:var(--band)}
.feeds-icon{left:94px;top:955px;width:46px;height:36px;background:#9a9a9a;border-radius:50% 40% 50% 50%}
.feeds-title{left:154px;top:955px;font-size:24px;font-weight:600;color:#6a6a6a}
.feeds-text{left:353px;top:959px;width:490px;font-size:9.5px;line-height:16px;color:#333}
.feeds-text u{color:#666}

.footer{left:0;top:1006px;width:939px;height:146px;background:linear-gradient(180deg,#f0f0f0,var(--footer))}
.foot-col{top:1034px}
.foot-col h3{font-size:11.5px;font-weight:400;color:var(--brand);margin-bottom:7px}
.foot-col li{list-style:none;font-size:9.3px;line-height:15.7px;color:#444}
.foot-brand{left:636px;top:1050px;display:flex;align-items:center;gap:6px;font-size:24px;font-weight:600;color:#9a9a9a}
.foot-brand i{width:14px;height:14px;border-radius:50%;background:#9a9a9a}
.social{top:1058px;width:19px;height:19px;border-radius:2px}
.foot-about{left:636px;top:1103px;width:206px;font-size:9px;line-height:12.5px;color:#444;text-align:justify}
.base{left:0;top:1152px;width:939px;height:48px;background:var(--base);display:flex;align-items:center;justify-content:center;font-size:9px;color:#444}
</style>
</head>
<body>

<header>
  <div class="abs topbar"></div>
  <div class="abs topbar-link" style="left:342px"><svg viewBox="0 0 12 12"><path d="M2 1l2 0 1 3-1.2 1a6 6 0 0 0 3.2 3.2L8 7l3 1v2c0 .6-.5 1-1 1A9 9 0 0 1 1 2c0-.5.4-1 1-1z"/></svg>888-9-nimbo58</div>
  <div class="abs topbar-link" style="left:460px"><svg viewBox="0 0 12 12"><path d="M6 1.5c3 0 5 1.7 5 3.8S9 9 6 9L3 11l.6-2.5C2 7.9 1 6.7 1 5.3 1 3.2 3 1.5 6 1.5z"/></svg>Live Chat</div>
  <div class="abs topbar-link" style="left:560px"><svg viewBox="0 0 12 12"><path d="M1 5l5-3 5 3v5H1z M2 5.3l4 2.6 4-2.6"/></svg>Email Us</div>
  <div class="abs topbar-link" style="left:662px"><svg viewBox="0 0 12 12"><path d="M1 3h5v1H2v6h6V7h1v4H1z M9 1l2 2-5 5H4V6z"/></svg>Get a Quote</div>
  <div class="abs topbar-link" style="left:778px"><svg viewBox="0 0 12 12"><circle cx="6" cy="3.5" r="2.5"/><path d="M1 11c0-3 2-4.5 5-4.5s5 1.5 5 4.5z"/></svg>Client Login</div>

  <div class="abs brand"><span class="brand-dot"></span>Nimbo58</div>

  <nav>
    <div class="abs nav-rule"></div>
    <div class="abs nav-item" style="left:342px"><div class="label">DEDICATED SERVERS</div><div class="sub">Met Vexon Servers</div></div>
    <div class="abs nav-sep" style="left:476px"></div>
    <div class="abs nav-item" style="left:500px"><div class="label">VIRTUAL SERVERS</div><div class="sub">OpenKV or Zar</div></div>
    <div class="abs nav-sep" style="left:616px"></div>
    <div class="abs nav-item" style="left:641px"><div class="label">CLOUD SERVERS</div><div class="sub">Vistra Enterprise</div></div>
    <div class="abs nav-sep" style="left:750px"></div>
    <div class="abs nav-item" style="left:775px"><div class="label">ABOUT NIMBO58</div><div class="sub">Learn about us</div></div>
  </nav>
  <div class="abs header-rule"></div>
</header>

<section>
  <div class="abs hero"></div>
  <div class="abs hero-art" role="img" aria-label="Three dark server tower units"></div>
  <h2 class="abs hero-title">why we're different?</h2>
  <div class="abs hero-rule"></div>
  <div class="abs hero-tags">Fast response times<span>I</span>Your needs Matter<span>I</span>Enterprise Solutions</div>
  <div class="abs hero-btn">More about our services</div>
  <div class="abs slide-dot active" style="left:720px">1</div>
  <div class="abs slide-dot" style="left:751px">2</div>
  <div class="abs slide-dot" style="left:782px">3</div>
  <div class="abs slide-dot" style="left:813px">4</div>
</section>

<main>
  <h1 class="abs h1" style="font-weight:400">Hybrid Solutions<small>(H1)</small></h1>
  <div class="abs h1-rule"></div>
  <h2 class="abs h2" style="font-weight:400">The best of both dedicated and cloud. <strong>$179/mo</strong><small>(H2)</small></h2>
  <p class="abs intro">Ut enim ad minim veniam, quis nostrud exercitation ullamco laboris nisi ut aliquip ex ea commodo consequat. Duis aute irure dolor in reprehenderit in voluptate velit esse cillum dolore eu fugiat nulla pariatur. Excepteur sint occaecat cupida tat non proident, sunt in culpa qui officia deserunt mollit anim id est laborum.</p>
  <div class="abs offer" role="img" aria-label="Special offers banner showing a row of data centre server racks"></div>
  <div class="abs offer-tab">View more Details</div>

  <p class="abs body-copy">Sed ut perspiciatis unde omnis iste natus error sit voluptatem accusantium doloremque laudantium, totam rem aperiam, eaque ipsa quae ab illo inventore veritatis et quasi architecto beatae vitae dicta sunt explicabo. Nemo enim ipsam voluptatem quia voluptas sit aspernatur aut odit aut fugit, sed quia consequuntur magni dolores eos qui ratione voluptatem sequi nesciunt. Neque porro quisquam est, qui dolorem ipsum quia dolor sit amet, consectetur, adipisci velit, sed quia non numquam eius modi tempora incidunt ut labore et dolore magnam aliquam quaerat voluptatem. Ut enim ad minima veniam, quis nostrum exercitationem ullam corporis suscipit laboriosam, nisi ut aliquid ex ea commodi consequatur. But I must explain to you how all this mistaken idea of denouncing pleasure and praising pain was born and I will give you a complete account of the system, and expound the actual teachings of the great explorer of the truth, the master-builder of human happiness. No one rejects, dislikes, or avoids pleasure itself, because it is pleasure, but because those who do not know how to pursue pleasure rationally encounter consequences that are extremely painful. Nor again is there anyone who loves or pursues or desires to obtain pain of itself, because it is pain, but because occasionally circumstances occur in which toil and pain can procure him some great pleasure. To take a trivial example, which of us ever undertakes laborious physical exercise, except to obtain some advantage from it? But who has any right to find fault with a man who chooses to enjoy a pleasure that has no annoying consequences, or one who avoids a pain that produces no resultant pleasure.</p>

  <div class="abs rule" style="top:720px"></div>
  <div class="abs sample-h1">Heading 1</div>
  <div class="abs sample-h2">Heading 2</div>
  <div class="abs sample-p">Paragraph</div>
  <div class="abs rule" style="top:810px"></div>

  <div class="abs avatar" role="img" aria-label="Customer portrait photo"></div>
  <div class="abs avatar-name">Marcus Hale</div>
  <div class="abs testimonial"></div>
  <div class="abs testimonial-arrow"></div>
  <h3 class="abs testimonial-title" style="font-weight:400">Customer Testimonials</h3>
  <div class="abs testimonial-rule"></div>
  <p class="abs testimonial-quote"><b>&ldquo;</b>Vestibulum at orci a eros molestie rutrum. Fusce interdum erat vel eros elementum vitae interdum massa varius. Morbi fermentum commodo nisi, id interdum mauris suscipit pellentesque. Morbi velit eros, accumsan ut faucibus at, viverra id mi.<b>&rdquo;</b></p>
</main>

<section>
  <div class="abs feeds"></div>
  <div class="abs feeds-icon" role="img" aria-label="Bird illustration"></div>
  <div class="abs feeds-title">Chirper Feeds</div>
  <p class="abs feeds-text">Sed ut perspiciatis unde omnis iste natus error sit <u>voluptatem accusantium doloremque laudantium</u>, totam rem aperiam, eaque ipsa quae.</p>
</section>

<footer>
  <div class="abs footer"></div>
  <div class="abs foot-col" style="left:94px"><h3>Main Navigation</h3><ul><li>Dedicated Servers</li><li>Virtual Servers</li><li>I Cloud Servers</li><li>About Nimbo58</li></ul></div>
  <div class="abs foot-col" style="left:224px"><h3>Additional Info</h3><ul><li>Terms of Service</li><li>Privacy Policy</li><li>Service Level Agreement</li><li>Referral Program</li><li>I Reseller Program</li></ul></div>
  <div class="abs foot-col" style="left:386px"><h3>Support Center</h3><ul><li>USA 888-9-nimbo58</li><li>Live Chat</li><li>Email Us</li><li>Get a Quote</li><li>Client Login</li></ul></div>
  <div class="abs foot-col" style="left:512px"><h3>Locations</h3><ul><li>Chicago, IL</li><li>Dallas, TX</li><li>Kansas City, MO</li><li>Los Angeles, CA</li><li>New York City, NY</li></ul></div>
  <div class="abs foot-brand"><i></i>Nimbo58</div>
  <div class="abs social" style="left:798px;background:#3b5a94"></div>
  <div class="abs social" style="left:826px;background:#5fb8e6"></div>
  <p class="abs foot-about">We are a company at technical people, not sales drones. We deliver data center services to You</p>
  <div class="abs base">Copyright © 2012 www.nimbo58.com.au &nbsp;&nbsp; All rights reserved.</div>
</footer>

</body>
</html>
```